Roofing Contractor business card redesign

I want to redesign my business card with a fresh, eye catching concept

Target Market(s)

Residential Roofing Clients, potential employees, and subcontractors.

Industry/Entity Type

Business

Colors

Designer to choose colors to be used in the design.

Requirements
Nice to have
• I just want something that's more pleasing to the eye. You can use a combination of either / or of my logos.

```html
<!DOCTYPE html>
<html lang="en">
<head>
<meta charset="utf-8">
<title>Steady Hands General Contractors – Business Card</title>
<link rel="stylesheet" href="https://fonts.googleapis.com/css2?family=Open+Sans:wght@700;800&display=swap">
<style>
  :root {
    --card-yellow: #ffc907;
    --brand-brown: #4a1a16;
    --accent-orange: #e8782a;
    --faint-gold: #e0ad12;
    --page-bg: #2b2b2d;
    --white: #ffffff;
  }
  * { box-sizing: border-box; margin: 0; padding: 0; }
  html, body {
    width: 1200px; height: 880px; overflow: hidden;
    background: var(--page-bg);
    font-family: "Open Sans", Arial, sans-serif;
  }
  .sheet {
    width: 1200px; height: 880px;
    display: flex; flex-direction: column; align-items: center; justify-content: center;
    gap: 40px;
  }
  .card {
    position: relative;
    width: 680px; height: 388px;
    border-radius: 22px;
    background: var(--card-yellow);
    overflow: hidden;
  }
  .brand {
    display: flex; align-items: center; gap: 14px;
    color: var(--brand-brown);
    font-weight: 800;
    line-height: 1;
  }
  .brand__dot {
    width: 52px; height: 52px; border-radius: 50%;
    background: var(--brand-brown);
    flex: none;
  }
  .brand__name { font-size: 54px; letter-spacing: -1px; }
  .legal-name {
    color: var(--brand-brown);
    font-weight: 700;
    text-shadow: 0 0 2px var(--white), 0 0 2px var(--white);
  }

  /* Front */
  .card--front .brand { position: absolute; left: 108px; top: 118px; }
  .card--front .legal-name { position: absolute; left: 174px; top: 190px; font-size: 26px; }
  .card--front .web {
    position: absolute; left: 250px; top: 274px;
    font-size: 26px; font-weight: 800; color: var(--brand-brown);
    text-shadow: 0 0 2px var(--white), 0 0 2px var(--white);
  }
  .arrow-mark { position: absolute; }
  .arrow-mark--top { right: 60px; top: 84px; }
  .arrow-mark--bottom { left: 66px; top: 272px; }

  /* Back */
  .card--back .art { position: absolute; inset: 0; }
  .card--back .brand { position: absolute; left: 40px; top: 40px; }
  .card--back .brand__name { font-size: 40px; }
  .card--back .brand__dot { width: 40px; height: 40px; }
  .card--back .legal-name { position: absolute; left: 60px; top: 94px; font-size: 19px; }
  .contact {
    position: absolute; left: 60px; top: 150px;
    color: var(--white); font-weight: 800; font-size: 27px; line-height: 1.35;
    text-shadow: 0 0 3px var(--brand-brown), 0 0 2px var(--brand-brown), 0 0 1px var(--brand-brown);
  }
</style>
</head>
<body>
<main class="sheet">

  <section class="card card--front" aria-label="Business card front">
    <div class="brand">
      <span class="brand__dot"></span>
      <span class="brand__name">Steady Hands</span>
    </div>
    <p class="legal-name">General Contractors, Inc.</p>
    <svg class="arrow-mark arrow-mark--top" width="150" height="34" viewBox="0 0 150 34" aria-hidden="true">
      <g fill="var(--brand-brown)">
        <rect x="0" y="6" width="70" height="22"/>
        <polygon points="98,3 86,17 98,31 108,31 96,17 108,3"/>
        <polygon points="120,3 108,17 120,31 130,31 118,17 130,3"/>
      </g>
    </svg>
    <svg class="arrow-mark arrow-mark--bottom" width="170" height="34" viewBox="0 0 170 34" aria-hidden="true">
      <g fill="var(--brand-brown)">
        <polygon points="0,3 12,17 0,31 10,31 22,17 10,3"/>
        <polygon points="22,3 34,17 22,31 32,31 44,17 32,3"/>
        <rect x="60" y="6" width="110" height="22"/>
      </g>
    </svg>
    <p class="web">SteadyHandsGC.com</p>
  </section>

  <section class="card card--back" aria-label="Business card back">
    <svg class="art" width="680" height="388" viewBox="0 0 680 388">
      <defs>
        <linearGradient id="crewTone" x1="0" y1="0" x2="1" y2="1">
          <stop offset="0" stop-color="#f3c25a"/>
          <stop offset="0.5" stop-color="#e8782a"/>
          <stop offset="1" stop-color="#6b2a1c"/>
        </linearGradient>
        <path id="taglineCurve" d="M250,382 Q450,310 672,226"/>
      </defs>
      <rect role="img" aria-label="Faint roof-frame backdrop" x="180" y="60" width="260" height="260" fill="var(--faint-gold)" opacity="0.35"/>
      <g role="img" aria-label="Illustration of a roofing crew with tools">
        <path d="M400,120 Q480,30 680,0 L680,240 L400,300 Z" fill="url(#crewTone)"/>
      </g>
      <path d="M150,388 Q420,310 680,180 L680,388 Z" fill="var(--brand-brown)"/>
      <text font-family="Open Sans, Arial, sans-serif" font-weight="700" font-size="17" fill="var(--white)">
        <textPath href="#taglineCurve" startOffset="8%">Quality Roofing, Installed by Hand</textPath>
      </text>
    </svg>
    <div class="brand">
      <span class="brand__dot"></span>
      <span class="brand__name">Steady Hands</span>
    </div>
    <p class="legal-name">General Contractors, Inc.</p>
    <p class="contact">(555) 318 - 2046<br>SteadyHandsGC.com</p>
  </section>

</main>
</body>
</html>
```